Buch-Cover für Schweden-Krimi
Eine wirklich wunderbare Zusammenarbeit! Schon der erste Entwurf von ihr hat mir richtig gut gefallen; anschließende Anregungen wurden sehr schnell und äußerst professionell umgesetzt. Moonwhale kann daher uneingeschränkt empfohlen werden!
Zielgruppe
Ich bin ein Krimi-Autor. Die Zielgruppe liest gerne Krimis (oder auch Thriller) und hat eine Vorliebe für den Norden / Skandinavien.
Aufgabenstellung
Der Schweden-Krimi mit dem Titel 'Wo Schatten ruhen. Inspektor Malmgrens letzter Tag' spielt in Värmland, eine recht einsame Gegend mit vielen Seen und viel Wald. Zwei junge Frauen, die auch der Suche nach Freiheit waren, werden auf einer kleinen Insel in einem See tot aufgefunden. Ihre Leichen wurden vergraben, doch so drapiert, dass von einer die Hand aus dem Erdreich schaut, die geöffnete Handfläche nach oben. Dieses Bild könnte sich gut auf dem Cover machen. Auch mit den Elementen See, Wald, Licht und Dunkel kann gespielt werden.
'Wo Schatten ruhen' ist der Haupttitel, der dementsprechend groß gedruckt werden sollte. Der Untertitel 'Inspektor Malmgrens letzter Tag' kann kleiner abgedruckt werden, ebenso die Genre-Bezeichnung 'Krimi' bzw. 'Kriminalroman'.
E-Book: Maße 1,6 : 1 (idealerweise 2560 x 1600 px)
Buch: 12,7 x 20,32 cm (Buchdicke steht noch nicht endgültig fest)

```html
<!DOCTYPE html>
<html lang="de">
<head>
<meta charset="utf-8">
<title>Wo Schatten ruhen – Buchcover</title>
<link rel="stylesheet" href="https://fonts.googleapis.com/css2?family=Rubik+Dirt&family=Roboto:wght@400;500&display=swap">
<style>
  :root {
    --page: #ffffff;
    --fog-top: #7fb2b4;
    --fog-mid: #4f8a8d;
    --forest-dark: #1d3536;
    --ground: #151f20;
    --ink-light: #f7f9f9;
    --line: rgba(200, 232, 232, 0.55);
  }
  * { margin: 0; padding: 0; box-sizing: border-box; }
  html, body {
    width: 848px; height: 1200px; overflow: hidden;
    background: var(--page);
  }
  .cover {
    position: absolute;
    left: 92px; top: 79px;
    width: 664px; height: 1062px;
    overflow: hidden;
    color: var(--ink-light);
  }
  .cover-photo {
    position: absolute; inset: 0;
    background:
      radial-gradient(ellipse 60% 40% at 70% 30%, rgba(160,205,205,0.55), transparent 70%),
      linear-gradient(180deg, var(--fog-mid) 0%, var(--fog-top) 30%, var(--fog-mid) 52%, var(--forest-dark) 68%, var(--ground) 100%);
  }
  .cover-lines {
    position: absolute; inset: 0;
    width: 664px; height: 1062px;
  }
  .author {
    position: absolute; top: 26px; left: 0; right: 0;
    text-align: center;
    font: 500 25px/1 "Roboto", sans-serif;
    letter-spacing: 0.5px;
  }
  .title {
    position: absolute; left: 28px; top: 104px;
    width: 620px;
    font-family: "Rubik Dirt", sans-serif;
    font-weight: 400;
    font-size: 106px;
    line-height: 114px;
    letter-spacing: -3px;
    text-transform: uppercase;
    white-space: nowrap;
  }
  .title span { display: block; }
  .subtitle {
    position: absolute; left: 30px; top: 462px;
    font: 400 38px/1 "Roboto", sans-serif;
    white-space: nowrap;
  }
  .genre {
    position: absolute; bottom: 26px; left: 0; right: 0;
    text-align: center;
    font: 500 25px/1 "Roboto", sans-serif;
  }
</style>
</head>
<body>
  <main class="cover">
    <div class="cover-photo" role="img" aria-label="Nebliger Wald in Blaugrün, im dunklen Waldboden ragt eine geöffnete Hand aus der Erde"></div>
    <svg class="cover-lines" viewBox="0 0 664 1062" aria-hidden="true">
      <line x1="510" y1="0" x2="300" y2="250" stroke="var(--line)" stroke-width="1"/>
      <line x1="300" y1="500" x2="664" y2="873" stroke="var(--line)" stroke-width="1"/>
      <line x1="430" y1="800" x2="664" y2="540" stroke="var(--line)" stroke-width="1"/>
      <line x1="170" y1="1000" x2="185" y2="1062" stroke="var(--line)" stroke-width="1"/>
    </svg>
    <p class="author">Kerstin Lund</p>
    <h1 class="title"><span>Wo</span><span>Schatten</span><span>ruhen</span></h1>
    <p class="subtitle">Inspektor Malmgrens letzter Tag</p>
    <p class="genre">Kriminalroman</p>
  </main>
</body>
</html>
```